Redesign of a facility management homepage

We need a redesign/an improved design of the facility management homepage (http://www.kolvenhaus-drefling.de/).
This websites offers detailed information on the "About us" as company, the "Services" provided and special information on facility and strata management. We would like to keep the structure of the website.
We need ideas/designs how this website could look more modern and confidential and appealing/pleasant for visitors at the same time and not losing the main purpose of information distribution.
The green color must be used since this is the basic color from our logo.
The blue in the background of the logo ist optional. So feel to use it or not.
We need no coding only design (.psd or as .ai)
Industry/Entity Type
It Company
Look and feel
Each slider illustrates characteristics of the customer's brand and the style your logo design should communicate.

```html
<!DOCTYPE html>
<html lang="en">
<head>
<meta charset="utf-8">
<title>KDH Office and Caretaker Service</title>
<link href="https://fonts.googleapis.com/css2?family=Roboto:wght@300;400;500;700&family=Open+Sans:wght@400;600&display=swap" rel="stylesheet">
<style>
:root{
  --green:#2e9147;
  --green-dark:#25803c;
  --text:#555;
  --heading:#404040;
  --nav:#555;
  --bg:#eeeeee;
  --line:#d6d6d6;
  --blue-grey:#5a7a98;
  --dark:#1d1d1d;
}
*{margin:0;padding:0;box-sizing:border-box}
html,body{width:1013px;height:1200px;overflow:hidden}
body{position:relative;background:var(--bg);font-family:"Roboto",Arial,sans-serif;color:var(--text)}
.abs{position:absolute}
.site-header{left:0;top:0;width:1013px;height:57px;background:#f1f1f1;border-bottom:1px solid #e2e2e2}
.brand{z-index:5;left:135px;top:0;width:103px;height:85px;background:linear-gradient(#e9f1f8,#c4d8ea);clip-path:polygon(0 0,100% 0,100% 72%,50% 100%,0 72%);display:flex;align-items:flex-start;justify-content:center;padding-top:22px;gap:5px}
.brand-mark{width:10px;height:10px;background:var(--green);margin-top:6px}
.brand-name{font-weight:700;font-size:22px;color:var(--green)}
.main-nav{left:271px;top:21px;display:flex;gap:15px;font-size:10px;letter-spacing:.2px;color:var(--nav)}
.main-nav .active{color:var(--green)}
.header-phone{left:795px;top:21px;font-size:10px;color:var(--nav);display:flex;align-items:center;gap:3px}
.hero-photo{left:0;top:57px;width:458px;height:321px;background:linear-gradient(100deg,#5d5f63 0%,#b5b8bd 35%,#e8ebee 60%,#f6f7f8 100%)}
.hero-right{left:458px;top:57px;width:555px;height:321px;background:#f6f6f6}
.vehicle-photo{left:457px;top:84px;width:421px;height:212px;background:linear-gradient(#a88860 0%,#cfd0cf 40%,#ececec 65%,#6b5a48 100%)}
.vehicle-caption{left:526px;top:241px;width:284px;height:41px;background:rgba(40,40,40,.82);color:#fff;font-weight:700;font-size:22px;text-align:center;line-height:41px}
.company-card{left:457px;top:296px;width:421px;height:170px;background:var(--green);color:#fff;padding:15px 22px}
.company-card h2{font-weight:500;font-size:13.5px;letter-spacing:.3px;margin-bottom:6px}
.company-card p{font-size:9.5px;font-weight:500;line-height:17.5px}
.contact-form-link{margin-top:5px;margin-left:2px;width:370px;height:23px;background:#e6eee2;color:#333;font-size:9.5px;font-weight:500;display:flex;align-items:center;gap:6px;padding-left:9px;border:1px solid #cfe0cc}
.welcome{left:135px;top:391px;width:305px}
.welcome h1{font-weight:300;font-size:21px;color:var(--blue-grey);margin-bottom:6px}
.welcome h1 strong{font-weight:700;color:var(--green)}
.welcome p{font-family:"Open Sans",sans-serif;font-size:9.5px;line-height:16.3px}
.read-more{color:var(--green);font-weight:600}
.divider{left:135px;top:494px;width:743px;height:1px;background:var(--line)}
.divider-dots{left:496px;top:492px;display:flex;gap:3px}
.divider-dots i{width:4px;height:4px;border-radius:50%;background:#c9c9c9}
.section-title{left:0;top:517px;width:1013px;text-align:center;font-weight:500;font-size:23px;color:var(--heading);letter-spacing:.3px}
.service{top:566px;width:230px;text-align:center}
.service svg{display:block;margin:0 auto}
.service h3{color:var(--green);font-weight:500;font-size:14px;margin:15px 0 4px;letter-spacing:.3px}
.service p{font-family:"Open Sans",sans-serif;font-size:9.5px;line-height:16.3px}
.cta-band{left:0;top:794px;width:1013px;height:191px;background:linear-gradient(90deg,#3e3e3f 0%,#5b5550 45%,#b7907a 75%,#7c6a5e 100%)}
.cta-title{left:0;top:810px;width:1013px;text-align:center;color:#fff;font-weight:300;font-size:30px;letter-spacing:.5px}
.cta-title strong{font-weight:700}
.cta-sub{left:0;top:848px;width:1013px;text-align:center;color:#fff;font-weight:500;font-size:11.5px;letter-spacing:.2px}
.quick-form{left:135px;top:884px;width:743px;height:72px;background:#fff;border-radius:2px;display:flex;align-items:center;padding:0 19px 0 21px;gap:10px}
.field{height:32px;border:1px solid #d8d8d8;border-radius:2px;font-size:11px;color:#999;display:flex;align-items:center;padding-left:14px}
.submit{width:94px;height:32px;background:var(--dark);color:#fff;font-weight:700;font-size:11px;border-radius:3px;display:flex;align-items:center;justify-content:center;gap:7px}
.footer-col h4{color:var(--green);font-weight:500;font-size:16.5px;margin-bottom:20px}
.footer-about{left:162px;top:1008px;width:268px}
.footer-about p{font-family:"Open Sans",sans-serif;font-size:9.5px;line-height:17px;text-align:justify}
.footer-links{left:477px;top:1008px;width:200px}
.link-grid{display:grid;grid-template-columns:118px 80px;font-family:"Open Sans",sans-serif;font-size:9.5px}
.link-grid span{height:27px;display:flex;align-items:center;padding-left:2px;border-bottom:1px solid #ddd}
.link-grid span:nth-last-child(-n+2){border-bottom:none}
.footer-follow{left:725px;top:1008px}
.social{display:flex;align-items:center;gap:11px;font-family:"Open Sans",sans-serif;font-size:9.5px;margin-bottom:5px}
.social i{width:27px;height:26px;background:var(--green);display:block}
.copyright{left:0;top:1167px;width:1013px;height:33px;background:var(--green);color:#fff;font-family:"Open Sans",sans-serif;font-size:10px;text-align:center;line-height:33px}
</style>
</head>
<body>
<header class="site-header abs"></header>
<div class="brand abs"><span class="brand-mark"></span><span class="brand-name">KDH</span></div>
<nav class="main-nav abs">
  <span class="active">HOME</span><span>ABOUT US</span><span>WE OVER US</span><span>BUILDING MANAGEMENT</span><span>LETTING</span><span>CONTACT US</span>
</nav>
<div class="header-phone abs">
  <svg width="7" height="10" viewBox="0 0 7 10"><rect width="7" height="10" rx="1" fill="#2e9147"/><rect x="1.5" y="1.5" width="4" height="5" fill="#fff"/></svg>
  0 41 52/7730 14
</div>

<div class="hero-photo abs" role="img" aria-label="Worker clearing snow with a snow blower on a residential street"></div>
<div class="hero-right abs"></div>
<div class="vehicle-photo abs" role="img" aria-label="Row of white company service vans parked on a cobbled lot"></div>
<div class="vehicle-caption abs">OUR VEHICLE PARK</div>
<section class="company-card abs">
  <h2>KDH OFFICE AND CARETAKER SERVICE GMBH</h2>
  <p>Marktweg 14 in 04712 Drefling represented by Mrs. Petra Lindqvist, Business guide</p>
  <p>AG Ostheim, Mr. No.: HBR 27519</p>
  <p>Tel.: 0 41 52 / 77 30 14</p>
  <p>Fax: 0 41 52 / 77 30 15</p>
  <p>Mail: info@kolvenhaus-drefling.de</p>
  <div class="contact-form-link">
    <svg width="12" height="8" viewBox="0 0 12 8"><rect width="12" height="8" fill="#2e9147"/><path d="M0 0 6 5 12 0" stroke="#e6eee2" fill="none"/></svg>
    Form for Contact
  </div>
</section>

<section class="welcome abs">
  <h1>WELCOME TO <strong>KDH</strong></h1>
  <p>Lorem ipsum dolor sit amet, consectetur adipiscing elit. Ut ut cursus tellus. Integer tempor ac lorem vitae condimentum. Vestibulum id erat tincidunt, adipiscing enim sit amet, sodales diam. <span class="read-more">Read More...</span></p>
</section>

<div class="divider abs"></div>
<div class="divider-dots abs"><i></i><i></i><i></i></div>

<h2 class="section-title abs">World-Class Service Provider</h2>

<div class="service abs" style="left:131px">
  <svg width="104" height="118" viewBox="0 0 104 118"><polygon points="52,0 104,29.5 104,88.5 52,118 0,88.5 0,29.5" fill="#2e9147"/>
    <path d="M32 72V58a20 20 0 0 1 40 0v14" stroke="#fff" stroke-width="6" fill="none"/>
    <rect x="27" y="60" width="10" height="18" rx="3" fill="#fff"/><rect x="67" y="60" width="10" height="18" rx="3" fill="#fff"/></svg>
  <h3>Disturbance On-Line Announce</h3>
  <p>Fusce vel commodo arcu. Sed vel urna id neque convallis laoreet. Ut ligula dui, accumsan nec varius sit amet, consectetur non ipsum.</p>
</div>
<div class="service abs" style="left:394px">
  <svg width="104" height="118" viewBox="0 0 104 118"><polygon points="52,0 104,29.5 104,88.5 52,118 0,88.5 0,29.5" fill="#2e9147"/>
    <path d="M34 38c4-4 8-3 10 1l4 8c1 3 0 5-2 7l-3 2c2 6 8 12 14 14l2-3c2-2 4-3 7-2l8 4c4 2 5 6 1 10-6 6-16 4-26-5s-20-24-15-36z" fill="#fff"/></svg>
  <h3 style="margin-top:18px">Contact</h3>
  <p>Fusce vel commodo arcu. Sed vel urna id neque convallis laoreet. Ut ligula dui, accumsan nec varius sit amet, consectetur non ipsum.</p>
</div>
<div class="service abs" style="left:653px">
  <svg width="104" height="118" viewBox="0 0 104 118"><polygon points="52,0 104,29.5 104,88.5 52,118 0,88.5 0,29.5" fill="#2e9147"/>
    <path d="M33 55 52 41 71 55" stroke="#fff" stroke-width="4" fill="none"/>
    <rect x="39" y="55" width="26" height="20" fill="none" stroke="#fff" stroke-width="3.5"/>
    <rect x="48" y="62" width="8" height="13" fill="#fff"/>
    <path d="M30 80q22 12 44 0" stroke="#fff" stroke-width="3.5" fill="none"/></svg>
  <h3 style="margin-top:18px">Imprint</h3>
  <p>Fusce vel commodo arcu. Sed vel urna id neque convallis laoreet. Ut ligula dui, accumsan nec varius sit amet, consectetur non ipsum.</p>
</div>

<div class="cta-band abs" role="img" aria-label="Customer support agent wearing a headset, softly blurred"></div>
<h2 class="cta-title abs">Need a Customer <strong>Solutions?</strong></h2>
<p class="cta-sub abs">we can help. Tell us about your project and we'll get in touch.</p>
<div class="quick-form abs">
  <div class="field" style="width:152px">Name</div>
  <div class="field" style="width:152px">Phone</div>
  <div class="field" style="width:274px">Message</div>
  <div class="submit">SUBMIT
    <svg width="11" height="11" viewBox="0 0 11 11"><circle cx="5.5" cy="5.5" r="5.5" fill="#fff"/><path d="M4.5 3 7 5.5 4.5 8z" fill="#1d1d1d"/></svg>
  </div>
</div>

<section class="footer-col footer-about abs">
  <h4>ABOUT KDH</h4>
  <p>Lorem ipsum dolor sit amet, consectetur adipiscing elit. Suspendisse a cursus odio. Praesent erat metus, dictum vel placerat sed, convallis eget nulla. Nulla dictum at elit at volutpat. Praesent posuere cursus fringilla. Pellentesque gravida, massa et pulvinar gravida, nisl nisl ultricies nisl, in laoreet erat lacus sed libero. <span class="read-more">Read More...</span></p>
</section>
<section class="footer-col footer-links abs">
  <h4>IMPORTANT LINKS</h4>
  <div class="link-grid">
    <span>Home</span><span>Letting</span>
    <span>About Us</span><span>Privacy policy</span>
    <span>We Over Us</span><span>FAQ</span>
    <span>Building Management</span><span>Contact us</span>
  </div>
</section>
<section class="footer-col footer-follow abs">
  <h4>FOLLOW US</h4>
  <div class="social"><i></i>Circleway</div>
  <div class="social"><i></i>Chatterly</div>
  <div class="social"><i></i>workvine</div>
</section>

<footer class="copyright abs">© 2014 Copyright kdh. All Rights reserved.</footer>
</body>
</html>
```